A poster of company Values to hand in our offices

I would like to have our corporate values and their detail, put on a poster that I can hang in our office for all to see every day. I would like it to be "cool" modern and edgy...if any of that makes sense :-) I have attached our values, our logo, + two examples of value posters i liked. Just for insight.
As background we are a software company that deals with a lot of complex math and code.

Target Market(s)

our employees

Industry/Entity Type

It Company

Other font styles liked:
• see notes

Requirements
Must have
• -Values must be on the poster
• -Use our colors where relevant as follows:
• MURLAZ
• ‘MURL’ font is Bauhaus93
• ‘AZ’ is in italics and font is Franklin Gothic Heavy
• Orange:
• C 0 M 70 Y 100 K 0
• R 243 G 109 B 32
• Blue:
• C 72 M 36 Y 0 K 0
• R 67 G 140 B 202
• Yellow:
• C 6 M 1 Y 91 K 0
• R 246 G 232 B 47
• Green:
• C 39 M 0 Y 100 K 0
• R 169 G 207 B 55
• Light Blue:
• C 49 M 0 Y 1 K 0
• R 114 G 208 B 242
• Green/Yellow overlap:
• C 33 M 0 Y 100 K 0
• R 184 G 212 B 50
• Green/Light Blue overlap:
• C 56 M 0 Y 100 K 0
• R 125 G 194 B 66
• Yellow/Orange overlap:
• C 0 M 54 Y 100 K 0
• R 247 G 140 B 29
• Orange/Light Blue overlap:
• C 64 M 25 Y 0 K 0
• R 84 G 159 B 215

```html
<!DOCTYPE html>
<html lang="en">
<head>
<meta charset="utf-8">
<title>MURLAZ Company Values Posters</title>
<link rel="stylesheet" href="https://fonts.googleapis.com/css2?family=Archivo+Narrow:wght@700&family=Libre+Franklin:wght@500;600&display=swap">
<style>
  :root {
    --orange: #f36d20;
    --blue: #438cca;
    --yellow: #f6e82f;
    --green: #a9cf37;
    --light-blue: #72d0f2;
    --green-yellow: #b8d432;
    --green-lightblue: #7dc242;
    --yellow-orange: #f78c1d;
    --sky: #6fb5ee;
    --olive: #6b5e14;
    --pale-yellow: #fdf29a;
    --teal-ink: #0f4a5e;
    --ink: #1c1c1c;
    --stage: #eeeeee;
  }
  * { box-sizing: border-box; margin: 0; padding: 0; }
  html, body { width: 1200px; height: 1200px; overflow: hidden; }
  body {
    background: var(--stage);
    font-family: "Libre Franklin", Arial, sans-serif;
    position: relative;
  }
  .poster {
    position: absolute;
    width: 298px;
    height: 464px;
    overflow: hidden;
    background: #fff;
  }
  .poster--intro      { left: 90px;  top: 101px; background: linear-gradient(180deg, var(--sky) 0%, #a6d0f3 35%, #fff 70%); }
  .poster--partner    { left: 447px; top: 101px; background: linear-gradient(180deg, var(--green-lightblue) 0%, #a6d66d 30%, #fff 62%); }
  .poster--adapt      { left: 809px; top: 101px; background: linear-gradient(180deg, var(--yellow) 0%, #faf19a 45%, #fffbe6 70%); }
  .poster--innovation { left: 90px;  top: 630px; background: linear-gradient(180deg, var(--yellow-orange) 0%, #f9b36a 40%, #fff 80%); }
  .poster--dignity    { left: 447px; top: 630px; background: linear-gradient(180deg, var(--green-yellow) 0%, #d2e57a 35%, #fff 75%); }
  .poster--integrity  { left: 809px; top: 630px; background: linear-gradient(180deg, var(--light-blue) 0%, #a8e2f7 40%, #fff 68%); }

  .poster__title {
    position: absolute;
    left: 20px;
    font-family: "Archivo Narrow", "Arial Narrow", sans-serif;
    font-weight: 700;
    text-transform: uppercase;
    line-height: 1;
    font-size: 33px;
  }
  .poster__body {
    position: absolute;
    left: 21px;
    width: 240px;
    font-size: 14px;
    line-height: 20px;
    color: var(--ink);
    font-weight: 600;
  }

  .poster--intro .poster__title { top: 37px; font-size: 25px; color: #fff; line-height: 28px; }
  .value-list { position: absolute; left: 22px; top: 143px; list-style: none; font-size: 15.5px; line-height: 22px; color: var(--ink); font-weight: 600; }
  .value-list li::before { content: "\2022"; margin-right: 8px; }
  .poster__note { position: absolute; left: 22px; top: 214px; font-size: 11px; line-height: 16px; color: var(--ink); font-weight: 600; width: 210px; }

  .poster--partner .poster__title { top: 36px; color: #fff; }
  .poster--partner .poster__body { top: 120px; }

  .poster--adapt .poster__title { top: 36px; color: var(--olive); }
  .poster--adapt .poster__body { top: 150px; width: 250px; }

  .poster--innovation .poster__title { top: 50px; color: var(--pale-yellow); }
  .poster--innovation .poster__body { top: 131px; width: 245px; }

  .poster--dignity .poster__title { top: 50px; color: var(--ink); left: 38px; }
  .poster--dignity .poster__body { top: 97px; left: 37px; width: 245px; }

  .poster--integrity .poster__title { top: 50px; color: var(--teal-ink); left: 28px; }
  .poster--integrity .poster__body { top: 97px; left: 28px; width: 250px; }

  .ribbon-area {
    position: absolute;
    left: 0;
    width: 298px;
  }
  .ribbon-area--bottom {
    bottom: 0;
    height: 130px;
    background: linear-gradient(180deg, rgba(255,255,255,0) 0%, var(--green) 25%, var(--yellow) 50%, var(--orange) 72%, var(--light-blue) 100%);
  }
  .ribbon-area--tall {
    bottom: 0;
    height: 190px;
    background: linear-gradient(180deg, rgba(255,255,255,0) 0%, var(--blue) 22%, var(--light-blue) 45%, var(--yellow) 62%, var(--orange) 80%, var(--green) 100%);
  }
  .ribbon-area--top {
    top: 0;
    height: 40px;
    background: linear-gradient(180deg, var(--green-lightblue) 0%, var(--yellow) 70%, rgba(246,232,47,0) 100%);
  }

  .wordmark {
    position: absolute;
    left: 37px;
    bottom: 66px;
    display: flex;
    align-items: center;
    gap: 10px;
    font-weight: 600;
    font-size: 32px;
    color: var(--orange);
    letter-spacing: 1px;
  }
  .wordmark__dot { width: 14px; height: 14px; border-radius: 50%; background: var(--blue); }
</style>
</head>
<body>

  <section class="poster poster--intro">
    <h2 class="poster__title">Today we create the<br>future by striving<br>to exceed in</h2>
    <ul class="value-list">
      <li>Customer Partnership</li>
      <li>Proactive Adaptation to Change</li>
      <li>Continuous Innovation</li>
    </ul>
    <p class="poster__note">All while maintaining the highest standards of dignity and integrity.</p>
    <div class="ribbon-area ribbon-area--bottom" role="img" aria-label="Decorative band of flowing coloured ribbons"></div>
  </section>

  <section class="poster poster--partner">
    <h2 class="poster__title">Customer<br>Partnership</h2>
    <p class="poster__body">We will work together with our customers, on an ongoing basis, to ensure our technology continues to add value to their operation, while also ensuring both their and our success.</p>
    <div class="wordmark"><span>MURLAZ</span><span class="wordmark__dot"></span></div>
  </section>

  <section class="poster poster--adapt">
    <h2 class="poster__title">Proactive<br>Adaptation<br>to Change</h2>
    <p class="poster__body">We will listen to our customers, and to the markets we are in, as well as watch for trends, impacts and changes, to foresee, embrace, and help shape what is to come. We will try to always stay ahead of the curve.</p>
    <div class="ribbon-area ribbon-area--tall" role="img" aria-label="Decorative band of flowing coloured ribbons"></div>
  </section>

  <section class="poster poster--innovation">
    <h2 class="poster__title">Continuous<br>Innovation</h2>
    <p class="poster__body">We will strive to provide ongoing upgrades and enhancements to our technologies. We will try to not fundamentally change the dynamics of our end users, but rather provide them superior value in their ongoing operations.</p>
    <div class="ribbon-area ribbon-area--bottom" role="img" aria-label="Decorative band of flowing coloured ribbons"></div>
  </section>

  <section class="poster poster--dignity">
    <div class="ribbon-area ribbon-area--top" role="img" aria-label="Decorative band of flowing coloured ribbons"></div>
    <h2 class="poster__title">Dignity</h2>
    <p class="poster__body">We will speak, write, and overall behave with self-respect and appreciation of the formality or gravity of a situation - no matter how hard or stressful - both internally and externally.</p>
    <div class="wordmark"><span>MURLAZ</span><span class="wordmark__dot"></span></div>
  </section>

  <section class="poster poster--integrity">
    <h2 class="poster__title">Integrity</h2>
    <p class="poster__body">We will always be honest and act with strong moral principles and uprightness. We will do so in all of our relationships with coworkers, customers and stakeholders. We will always behave with, and in turn, assume positive intent.</p>
    <div class="ribbon-area ribbon-area--tall" role="img" aria-label="Decorative band of flowing coloured ribbons"></div>
  </section>

</body>
</html>
```